Business Card cabinets and cabinets components making company.

the card should be formal and interesting at the same time. The main colors will be black and white.

Font styles to use
Sans Serif

Colors

Designer to choose only greyscale colors for use in the design.

Requirements
Must have
• At least must have the followings:
office phone
cell phone
address
position
name
email
web

```html
<!DOCTYPE html>
<html lang="en">
<head>
<meta charset="utf-8">
<title>Trimwell Business Card</title>
<link rel="stylesheet" href="https://fonts.googleapis.com/css2?family=Open+Sans:wght@400;700&display=swap">
<style>
  :root {
    --backdrop: #3f3834;
    --card: #1f1f1f;
    --ink: #ffffff;
    --silver: #b9b9b9;
    --rule: #8a8a8a;
  }
  * { margin: 0; padding: 0; box-sizing: border-box; }
  html, body { width: 1200px; height: 795px; overflow: hidden; }
  body {
    background: var(--backdrop);
    font-family: "Open Sans", Arial, sans-serif;
    position: relative;
  }
  .card {
    position: absolute;
    top: 250px;
    width: 520px;
    height: 297px;
    background: var(--card);
    border-radius: 6px;
    box-shadow: 0 6px 18px rgba(0,0,0,.45);
    color: var(--ink);
  }
  .card--front { left: 50px; }
  .card--back { left: 630px; }

  /* Front */
  .brand {
    display: flex; align-items: center; gap: 12px;
    font-weight: 700; letter-spacing: .5px;
  }
  .brand__mark { display: block; border: 3px solid currentColor; }
  .card--front .brand {
    position: absolute; left: 0; right: 0; top: 112px;
    justify-content: center;
    font-size: 50px; color: var(--silver);
  }
  .card--front .brand__mark { width: 34px; height: 34px; }
  .card--front .brand-rule {
    position: absolute; left: 100px; right: 100px; top: 186px;
    height: 2px; background: var(--rule);
  }

  /* Back */
  .person { position: absolute; left: 34px; top: 34px; }
  .person__name { font-size: 17px; font-weight: 700; text-transform: uppercase; letter-spacing: .3px; }
  .person__role { font-size: 13px; color: #d8d8d8; }
  .contact { position: absolute; left: 34px; top: 100px; list-style: none; }
  .contact li {
    display: flex; align-items: center; gap: 7px;
    font-size: 14px; line-height: 21px;
  }
  .contact svg { width: 12px; height: 12px; flex: none; }
  .card--back .brand {
    position: absolute; right: 32px; top: 44px;
    font-size: 38px; color: var(--ink); gap: 9px;
  }
  .card--back .brand__mark { width: 26px; height: 26px; }
  .card--back .brand-rule {
    position: absolute; right: 32px; width: 170px; top: 104px;
    height: 2px; background: var(--ink);
  }
  .divider {
    position: absolute; left: 40px; right: 32px; top: 198px;
    height: 2px; background: var(--ink);
  }
  .address {
    position: absolute; right: 32px; top: 216px;
    text-align: right; font-size: 15px; line-height: 22px; font-style: normal;
  }
</style>
</head>
<body>
  <section class="card card--front" aria-label="Card front">
    <div class="brand"><span class="brand__mark"></span><span class="brand__name">Trimwell</span></div>
    <div class="brand-rule"></div>
  </section>

  <section class="card card--back" aria-label="Card back">
    <div class="person">
      <p class="person__name">Dorian Hale</p>
      <p class="person__role">Founder &amp; CEO</p>
    </div>
    <ul class="contact">
      <li>
        <svg viewBox="0 0 12 12" fill="none" stroke="#fff" stroke-width="1.3"><path d="M2.5 1.5l2 .3.6 2-1.2 1a6 6 0 0 0 2.8 2.8l1-1.2 2 .6.3 2c-.2.7-.9 1-1.6 1A8 8 0 0 1 1.5 3c0-.7.3-1.3 1-1.5z"/></svg>
        (555) 014-2290
      </li>
      <li>
        <svg viewBox="0 0 12 12" fill="none" stroke="#fff" stroke-width="1.3"><rect x="3" y="1" width="6" height="10" rx="1"/><path d="M5.3 9.2h1.4"/></svg>
        (555) 014-7731
      </li>
      <li>
        <svg viewBox="0 0 12 12" fill="#fff"><path d="M1 2.5h10v7H1z"/><path d="M1 2.5l5 4 5-4" fill="none" stroke="#1f1f1f" stroke-width="1"/></svg>
        info@trimwellcabinets.com
      </li>
      <li>
        <svg viewBox="0 0 12 12" fill="none" stroke="#fff" stroke-width="1.1"><circle cx="6" cy="6" r="5"/><ellipse cx="6" cy="6" rx="2.2" ry="5"/><path d="M1 6h10"/></svg>
        www.trimwellcabinets.com
      </li>
    </ul>
    <div class="brand"><span class="brand__mark"></span><span class="brand__name">Trimwell</span></div>
    <div class="brand-rule"></div>
    <div class="divider"></div>
    <address class="address">Address line, Suite code<br>State, 3573, Country</address>
  </section>
</body>
</html>
```